wine label design

i'm a fine wine store based in new zealand which buys quality bulk wine and bottles it, passing on the significant savings onto the customer. i require a brand name and design which is cool/ sharp and contempory. the wines will be all still wines, there won't be any sparkling wines under this brand. i've used brand names like harbourlight wine company for previous designs/label but want something more edgier. we thought about a brand name 'sky above the vines' or 'harbourlight wine co' but couldn't get a design to match the title of brand, if you have any thoughts on this send thru your design. take into account color they have to be bold as i am printing these thru a digital printer. the label is a wrap around design, the dimensions are approximately 80 or 90 mm high and 210 mm wide. have a look at these links, i think they have some x-factor to them: http://www.marlowvale.example/store/product_images/p/855/velora__34476_zoom.jpg: OR

http://static3.cellarfinder.example/images/labels/35/24/ember-in-the-fog-shiraz-petite-sirah-south-australia-10203524.jpg: OR

http://www.bottlebarn.example/ui/productimages/25223/25223_w240.jpg: OR

http://www.vintrail.example/images/viewWinery.php?pic=238291

Take into account i have to be able put a wine desription on the back label, barcode and a few technical details required by law. on the front label all i require is space to put the grape variety, area and vintage. i need the grape type to really stand out.
Updates

Reason: hi, the designs coming thru look good, just need a little more changes, also please read thru the brief, there are a few things i have noted such as label size etc etc

Target Market(s)

am after a label the cool/edgy/contempoary that appeals to the educated well off customer that willing to give something new a go by the look of the label that is cool and edgy.

Industry/Entity Type

Boutique

Requirements
Must have
• bold bold bold, it must stand out on the shelf
Nice to have
• a title/brand name that links what i'm doing, from what i'm doing the name 'harbourlight wine co' is probably best suited.
Should not have
• basic boring artwork and small text, the bigger the text the better

```html
<!DOCTYPE html>
<html lang="en">
<head>
<meta charset="utf-8">
<title>Harbor Calm — wine labels</title>
<link rel="stylesheet" href="https://fonts.googleapis.com/css2?family=Archivo:wdth,wght@87.5,700;87.5,800&display=swap">
<style>
  :root {
    --page: #ffffff;
    --label-ground: #000000;
    --merlot-fill: #9e0f4e;
    --merlot-line: #d3145f;
    --merlot-band: #c70f5b;
    --grigio-fill: #b2b11c;
    --grigio-line: #e8e862;
    --grigio-band: #8d8c08;
    --band-text: #ffffff;
  }
  html, body {
    margin: 0;
    padding: 0;
    width: 1200px;
    height: 900px;
    overflow: hidden;
    background: var(--page);
  }
  .sheet {
    position: relative;
    width: 1200px;
    height: 900px;
  }
  .label {
    position: absolute;
    left: 122px;
    width: 952px;
    height: 406px;
    background: var(--label-ground);
    overflow: hidden;
  }
  .label--merlot { top: 36px; }
  .label--grigio { top: 454px; }
  .label svg { display: block; width: 952px; height: 406px; }
  .brand {
    font-family: "Archivo", "Helvetica Neue", Arial, sans-serif;
    font-stretch: 87.5%;
    font-weight: 800;
    font-size: 132px;
    stroke-width: 3.5;
    stroke-linejoin: round;
  }
  .label--merlot .brand { fill: var(--merlot-fill); stroke: var(--merlot-line); }
  .label--grigio .brand { fill: var(--grigio-fill); stroke: var(--grigio-line); }
  .variety-band--merlot { fill: var(--merlot-band); }
  .variety-band--grigio { fill: var(--grigio-band); }
  .variety {
    font-family: "Archivo", "Helvetica Neue", Arial, sans-serif;
    font-weight: 700;
    font-size: 14px;
    letter-spacing: 4px;
    fill: var(--band-text);
  }
</style>
</head>
<body>
<main class="sheet">
  <section class="label label--merlot">
    <svg viewBox="0 0 952 406" aria-label="Harbor Calm Merlot label">
      <text class="brand" x="476" y="294" textLength="474" lengthAdjust="spacingAndGlyphs">HARBOR</text>
      <text class="brand" x="476" y="396" textLength="290" lengthAdjust="spacingAndGlyphs">CALM</text>
      <rect class="variety-band--merlot" x="752" y="350" width="200" height="38"/>
      <text class="variety" x="884" y="374" text-anchor="middle">MERLOT</text>
    </svg>
  </section>

  <section class="label label--grigio">
    <svg viewBox="0 0 952 406" aria-label="Harbor Calm Pinot Grigio label">
      <text class="brand" x="476" y="294" textLength="474" lengthAdjust="spacingAndGlyphs">HARBOR</text>
      <text class="brand" x="476" y="396" textLength="290" lengthAdjust="spacingAndGlyphs">CALM</text>
      <rect class="variety-band--grigio" x="754" y="348" width="198" height="38"/>
      <text class="variety" x="842" y="372" text-anchor="middle">PINOT GRIGIO</text>
    </svg>
  </section>
</main>
</body>
</html>
```